Leading car website needs banner ads + EDM

We are looking for a freelance graphic/web designer to create a set of 5 web banners and an EDM design, with associated HTML markup, to promote a competition for our leading car reviews website (http://www.motorvista.example). We are trying to promote a competition which encourages users to enter their own car reviews (i.e via: http://www.motorvista.example/reader-reviews/), with $1000 and $100 fuel vouchers (Veltrop Gaspoint) as the incentive.
We are essentially looking for one banner ad in 5 different sizes:
640x320 (static)
600x300 (static)
300x90 (animated)
300x250 (animated)
728x90 (animated)
+ an EDM newsletter which can be sent out to our database of users.
Ideally 3 of the ads will be made as animated gifs, with three frames of text that rotates. The text will be to the effect of:
1. "REVIEW YOUR CAR ON MOTORVISTA TO WIN!"
2. "WIN $1,000 PETROL"
3. "$1,000 FUEL EVERY MONTH +$100 FUEL EVERY WEEK"
*NOTE: All banners should also include "*Terms and conditions apply" in small, but visible, print somewhere on 1 frame
Designs among all banners and the EDM should use a consistant colour scheme and styling. All designs should include the motor vista logo as attached (on black OR white background) and an image of the Veltrop Gaspoint cards (the prize), as attached.
EDM: Should be 600 pixels wide and as deep as necessary to include the required header, copy and footer. The body background of the EDM should be white, in keeping with the website, using the logo on white background. The body should comprise of a header banner which is in the same style as the 640x320 (mentioned above), but only 600x300 in size. The main body copy is attached to this project in a word doc. The EDM should include a footer in similar styling as the footer used on the website (http://www.motorvista.example). There should be a graphical link to the website with the title "Add a User Review" and also a text link to "Terms and Conditions".
The EDM should be supplied in html format, along with all associated images.
Requirements
Must have
- - Must use motorvista logo
- Strong call to action
- All banners should also include "*Terms and conditions apply" in small, but visible, print somewhere on 1 frame
- Gaspoint image
Should not have
- - Strobe or flashing animation

```html
<!DOCTYPE html>
<html lang="en">
<head>
<meta charset="utf-8">
<title>Motorvista reader review banners – type options</title>
<link rel="stylesheet" href="https://fonts.googleapis.com/css2?family=Arimo:wght@400;700&family=Anton&family=Mada:wght@400;700&display=swap">
<style>
  :root {
    --board-top: #3c3f43;
    --board-mid: #9ba0a5;
    --board-bottom: #4b4e52;
    --label: #ffffff;
    --panel-dark: #1c1c1d;
    --panel-glow: #2c2c2e;
    --paper: #ffffff;
    --orange: #f7941d;
    --orange-dark: #d96f00;
    --text-light: #ffffff;
    --terms: #b9b9b9;
    --brand-blue: #1f3348;
    --brand-red: #d71920;
  }
  * { box-sizing: border-box; margin: 0; padding: 0; }
  html, body { width: 760px; height: 1200px; overflow: hidden; }
  body {
    position: relative;
    background:
      radial-gradient(ellipse 70% 45% at 50% 55%, rgba(170,175,180,.55), transparent 70%),
      linear-gradient(180deg, var(--board-top) 0%, #6a6e73 20%, var(--board-mid) 55%, #6c7075 85%, var(--board-bottom) 100%);
    font-family: "Arimo", Arial, sans-serif;
  }
  .option-label {
    position: absolute; left: 77px;
    color: var(--label); font-size: 16px; font-family: "Arimo", Arial, sans-serif;
  }
  .banner {
    position: absolute; width: 600px; height: 298px; overflow: hidden;
    background: radial-gradient(ellipse 65% 75% at 35% 40%, var(--panel-glow), var(--panel-dark) 75%);
    box-shadow: 0 2px 6px rgba(0,0,0,.35);
  }
  .paper-curve { position: absolute; left: 0; top: 0; width: 600px; height: 300px; }
  .vehicle-photo {
    position: absolute; left: 340px; top: 18px; width: 260px; height: 280px;
    clip-path: polygon(30% 0, 100% 0, 100% 100%, 36% 100%, 0 55%, 8% 12%);
    background: radial-gradient(ellipse at 45% 45%, #3a3c40 0%, #161618 60%, #0a0a0b 100%);
  }
  .terms {
    position: absolute; right: 22px; top: 11px; z-index: 2;
    font-size: 9.5px; color: var(--terms);
  }
  .brand-mark {
    position: absolute; left: 24px; top: 28px;
    color: var(--orange); font-weight: 700; font-size: 27px; letter-spacing: .5px;
  }
  .headline {
    position: absolute; left: 34px; width: 310px; top: 86px;
    text-align: center; color: var(--text-light);
  }
  .headline .lead { font-size: 17px; line-height: 24px; margin-bottom: 6px; }
  .headline .prize { font-size: 20px; line-height: 29px; }
  .headline b { font-weight: 700; }
  .cta {
    position: absolute; left: 193px; top: 222px; width: 178px; height: 40px;
    border-radius: 8px;
    background: linear-gradient(180deg, #fbb040 0%, var(--orange) 45%, var(--orange-dark) 100%);
    box-shadow: 0 2px 4px rgba(0,0,0,.3);
    color: var(--text-light); font-weight: 700; font-size: 14px;
    display: flex; align-items: center; justify-content: center;
  }
  .sponsor {
    position: absolute; left: 26px; top: 252px;
    display: flex; align-items: center; gap: 8px;
    color: var(--brand-blue); font-weight: 700; font-size: 17px;
  }
  .sponsor .dot { width: 26px; height: 26px; border-radius: 50%; background: var(--brand-red); }

  .option-helvetica { left: 75px; top: 90px; }
  .option-impact { left: 75px; top: 452px; }
  .option-aller { left: 78px; top: 814px; height: 300px; }

  .option-impact .headline .prize { font-family: "Anton", Impact, sans-serif; font-weight: 400; font-size: 21px; }
  .option-impact .headline .prize b { font-weight: 400; }
  .option-aller, .option-aller .headline, .option-aller .cta, .option-aller .sponsor, .option-aller .brand-mark, .option-aller .terms { font-family: "Mada", "Trebuchet MS", sans-serif; }
  .option-aller .headline .prize { font-size: 21px; }
</style>
</head>
<body>

<p class="option-label" style="top:56px">Helvetica</p>
<section class="banner option-helvetica">
  <svg class="paper-curve" viewBox="0 0 600 300" aria-hidden="true"><path d="M0 194 Q230 250 600 200 L600 300 L0 300Z" fill="#fff"/></svg>
  <div class="vehicle-photo" role="img" aria-label="Black luxury SUV, front three-quarter view"></div>
  <p class="terms">Terms and conditions apply</p>
  <p class="brand-mark">MOTORVISTA</p>
  <div class="headline">
    <p class="lead">Review your car and <b>WIN</b></p>
    <p class="prize"><b>$1,000</b> FUEL <b>every month</b><br><b>+$100</b> FUEL <b>every week</b></p>
  </div>
  <a class="cta">Add a reader review</a>
  <div class="sponsor"><span class="dot"></span>Gaspoint</div>
</section>

<p class="option-label" style="top:418px">Helvetica + Impact</p>
<section class="banner option-impact">
  <svg class="paper-curve" viewBox="0 0 600 300" aria-hidden="true"><path d="M0 194 Q230 250 600 200 L600 300 L0 300Z" fill="#fff"/></svg>
  <div class="vehicle-photo" role="img" aria-label="Black luxury SUV, front three-quarter view"></div>
  <p class="terms">Terms and conditions apply</p>
  <p class="brand-mark">MOTORVISTA</p>
  <div class="headline">
    <p class="lead">Review your car and <b>WIN</b></p>
    <p class="prize">$1,000 FUEL every month<br>+$100 FUEL every week</p>
  </div>
  <a class="cta">Add a reader review</a>
  <div class="sponsor"><span class="dot"></span>Gaspoint</div>
</section>

<p class="option-label" style="top:780px">Aller</p>
<section class="banner option-aller">
  <svg class="paper-curve" viewBox="0 0 600 300" aria-hidden="true"><path d="M0 194 Q230 250 600 200 L600 300 L0 300Z" fill="#fff"/></svg>
  <div class="vehicle-photo" role="img" aria-label="Black luxury SUV, front three-quarter view"></div>
  <p class="terms">Terms and conditions apply</p>
  <p class="brand-mark">MOTORVISTA</p>
  <div class="headline">
    <p class="lead">Review your car and <b>WIN</b></p>
    <p class="prize"><b>$1,000</b> FUEL <b>every month</b><br><b>+$100</b> FUEL <b>every week</b></p>
  </div>
  <a class="cta">Add a reader review</a>
  <div class="sponsor"><span class="dot"></span>Gaspoint</div>
</section>

</body>
</html>
```